Tide Harbor Finance Business Cards

Looking for a business card for a new mortgage broking business. Name of the business is Tide Harbor Finance. Purpose of the business is to build trust and strong relationships with clients to then assist them with your mortgage lending needs. Most relationships within the business start off as an enquiry, and then can evolve into a 10+ year relationship, servicing clients from purchasing a new home to then upgrading for their family and even then assisting their children with their first home purchase. Business card should communicate financial security and trust.

Target Market(s)

Targeting professional clients who are looking to build a relationship with a knowledgeable mortgage professional

Industry/Entity Type

Finance - Home Loans

Contact Information for Business Card

Peter Colburn, Director, mobile: 0427 903186, email:peter@tideharborfinance.com.au, website: www.tideharborfinance.com.au

Font styles to use
Sans Serif

Requirements
Must have
• On the front: Must have company logo, contact details as above. On the back: slogan, 'full of choices, free of stress', plus listing services offered: home loans, investment loans, first home buyers, refinancing, car finance

```html
<!DOCTYPE html>
<html lang="en">
<head>
<meta charset="utf-8">
<title>Tide Harbor Finance – Business Cards</title>
<link rel="stylesheet" href="https://fonts.googleapis.com/css2?family=Inter:wght@400;500;700;800&display=swap">
<style>
  :root {
    --navy: #005177;
    --white: #ffffff;
    --soft-white: rgba(255, 255, 255, 0.82);
    --backdrop: #959595;
  }
  * { margin: 0; padding: 0; box-sizing: border-box; }
  html, body {
    width: 1200px; height: 1200px; overflow: hidden;
    background: var(--backdrop);
    font-family: "Inter", Arial, sans-serif;
  }
  .card {
    position: absolute;
    left: 179px;
    width: 861px;
    height: 495px;
    background: var(--navy);
    color: var(--white);
  }
  .card--front { top: 84px; }
  .card--back { top: 622px; }

  /* front */
  .front-brand {
    position: absolute;
    left: 0; right: 0; top: 146px;
    display: flex; align-items: center; justify-content: center;
    gap: 28px;
  }
  .brand-square {
    width: 130px; height: 130px;
    border: 8px solid var(--white);
    border-radius: 22px;
  }
  .brand-name {
    font-weight: 800;
    font-size: 60px;
    line-height: 1.02;
    letter-spacing: -1px;
    text-transform: uppercase;
    color: var(--white);
  }
  .slogan {
    position: absolute;
    left: 0; right: 0; top: 380px;
    text-align: center;
    font-size: 21px; font-weight: 500;
    letter-spacing: 2px;
    text-transform: uppercase;
  }
  .service-list {
    position: absolute;
    left: 0; right: 0; top: 424px;
    display: flex; justify-content: center; gap: 14px;
    list-style: none;
    font-size: 14px; font-weight: 400;
    letter-spacing: 1px;
    text-transform: uppercase;
    color: var(--soft-white);
  }
  .service-item + .service-item::before {
    content: "•";
    margin-right: 14px;
  }

  /* back */
  .brand-tile {
    position: absolute;
    left: 39px; top: 106px;
    width: 255px; height: 281px;
    background: var(--white);
    border-radius: 24px;
    display: flex; align-items: center; justify-content: center;
  }
  .brand-tile .brand-name {
    color: var(--navy);
    font-size: 30px;
    letter-spacing: -0.5px;
  }
  .person-name {
    position: absolute;
    left: 329px; top: 124px;
    font-size: 33px; font-weight: 700;
    letter-spacing: 0.5px;
  }
  .person-role {
    position: absolute;
    left: 329px; top: 166px;
    font-size: 22px; font-weight: 500;
    letter-spacing: 2.5px;
  }
  .divider {
    position: absolute;
    left: 329px; top: 205px;
    width: 361px; height: 2px;
    background: var(--white);
  }
  .contact-list {
    position: absolute;
    left: 325px; top: 240px;
    list-style: none;
  }
  .contact-item {
    display: flex; align-items: center;
    height: 30px;
    margin-bottom: 18px;
    font-size: 21px; font-weight: 500;
    letter-spacing: 2.4px;
  }
  .contact-icon {
    width: 27px; height: 27px;
    margin-right: 12px;
    flex: none;
  }
</style>
</head>
<body>
  <section class="card card--front">
    <div class="front-brand">
      <div class="brand-square"></div>
      <div class="brand-name">Tide<br>Harbor<br>Finance</div>
    </div>
    <p class="slogan">Full of choices, free of stress</p>
    <ul class="service-list">
      <li class="service-item">Home Loans</li>
      <li class="service-item">Investment Loans</li>
      <li class="service-item">First Home Buyers</li>
      <li class="service-item">Refinancing</li>
      <li class="service-item">Car Finance</li>
    </ul>
  </section>

  <section class="card card--back">
    <div class="brand-tile">
      <div class="brand-name">Tide<br>Harbor<br>Finance</div>
    </div>
    <h1 class="person-name">Peter Colburn</h1>
    <p class="person-role">Director</p>
    <div class="divider"></div>
    <ul class="contact-list">
      <li class="contact-item">
        <svg class="contact-icon" viewBox="0 0 24 24" fill="none" stroke="#fff" stroke-width="2" stroke-linecap="round" stroke-linejoin="round">
          <path d="M22 16.9v3a2 2 0 0 1-2.2 2 19.8 19.8 0 0 1-8.6-3.1 19.5 19.5 0 0 1-6-6A19.8 19.8 0 0 1 2.1 4.2 2 2 0 0 1 4.1 2h3a2 2 0 0 1 2 1.7c.1 1 .4 1.9.7 2.8a2 2 0 0 1-.5 2.1L8 9.9a16 16 0 0 0 6 6l1.3-1.3a2 2 0 0 1 2.1-.4c.9.3 1.8.6 2.8.7a2 2 0 0 1 1.7 2z"/>
          <path d="M15 2a7 7 0 0 1 7 7M15 6a3 3 0 0 1 3 3"/>
        </svg>
        0427 903186
      </li>
      <li class="contact-item">
        <svg class="contact-icon" viewBox="0 0 24 24" fill="#fff">
          <path d="M2 6h20v12H2z"/>
          <path d="M2 6l10 7 10-7" fill="none" stroke="#005177" stroke-width="1.6"/>
        </svg>
        peter@tideharborfinance.com.au
      </li>
      <li class="contact-item">
        <svg class="contact-icon" viewBox="0 0 24 24" fill="none" stroke="#fff" stroke-width="1.8">
          <circle cx="12" cy="12" r="10"/>
          <ellipse cx="12" cy="12" rx="4.5" ry="10"/>
          <path d="M2 12h20M4 7h16M4 17h16"/>
        </svg>
        www.tideharborfinance.com.au
      </li>
    </ul>
  </section>
</body>
</html>
```